Computer Sales and Repairs business, 1/4 and 1/2 page advertisement

We need a 1/4 and 1/2 page advertisement for our business. We want to show what we do, contact information and brands that we are an authorised repair centre for.

Our current colour scheme is green and orange (as shown in the attached logo) however we are open to other colours that would stand out on a newspaper page.

We're looking for designs that aren't crowded/busy, not boxy, possibly a flat colour design.

For example computer/laptop images (if needed) we use the following pc cases and business class laptop such as:

http://q41752.shop.brelvanotech.example/OzStore/Items/Item.aspx?id=K7W81TR&opt=&sel=MKD
http://vortelplay.example/index_ss.php?id=603
http://vortelplay.example/index_ss.php?id=404

Dimensions for 1/4 page ad:

85mm D x 220mm W (allow for 15mm bleed area on bottom, left and right)

Industry/Entity Type

It Company

Font styles to use
Sans Serif

Colors

Designer to choose colors to be used in the design.

Requirements
Should not have
• Should not be crowded/busy or boxy

```html
<!DOCTYPE html>
<html lang="en">
<head>
<meta charset="utf-8">
<title>Circuitwise Technicians – Computer Service Advertisement</title>
<link href="https://fonts.googleapis.com/css2?family=Open+Sans:wght@400;500;600;700;800&display=swap" rel="stylesheet">
<style>
  :root {
    --brand-green: #12673a;
    --brand-orange: #f4821f;
    --offer-red: #d3212b;
    --ink: #232323;
    --paper-light: #f4f5f6;
    --paper-mid: #dfe2e5;
    --white: #ffffff;
    --case-dark: #1d1f22;
    --case-mid: #4a4e54;
  }
  * { box-sizing: border-box; margin: 0; padding: 0; }
  html, body { width: 1200px; height: 885px; overflow: hidden; }
  body {
    font-family: "Open Sans", Arial, sans-serif;
    color: var(--ink);
    background: var(--white);
  }
  .ad {
    position: relative;
    width: 1200px;
    height: 885px;
    overflow: hidden;
    background: radial-gradient(ellipse at 50% 35%, var(--paper-light) 0%, var(--paper-mid) 100%);
  }
  .circuit-backdrop {
    position: absolute; inset: 0;
    background:
      radial-gradient(ellipse at 12% 35%, rgba(255,255,255,.7) 0%, rgba(255,255,255,0) 35%),
      radial-gradient(ellipse at 90% 40%, rgba(255,255,255,.7) 0%, rgba(255,255,255,0) 35%);
  }
  .headline {
    position: absolute; left: 0; right: 0; top: 40px;
    text-align: center;
    color: var(--brand-green);
    font-weight: 800;
    font-size: 94px;
    line-height: 86px;
    letter-spacing: -2px;
  }
  .subhead {
    position: absolute; left: 0; right: 0; top: 226px;
    text-align: center;
    font-size: 54px;
    line-height: 74px;
    font-weight: 500;
    letter-spacing: -1.5px;
    color: var(--ink);
  }
  .services-label {
    position: absolute; left: 238px; top: 334px;
    color: var(--brand-green);
    font-weight: 800;
    font-size: 29px;
    line-height: 40px;
  }
  .services-list {
    position: absolute; left: 462px; top: 338px;
    list-style: none;
    font-size: 20px;
    line-height: 28px;
  }
  .services-list li {
    position: relative;
    padding-left: 22px;
    margin-bottom: 14px;
  }
  .services-list svg { position: absolute; left: 0; top: 6px; }
  .offer {
    position: absolute; left: 805px; top: 343px;
    width: 312px; height: 232px;
    border: 5px dashed var(--brand-green);
    text-align: center;
    padding-top: 10px;
  }
  .offer-title { color: var(--offer-red); font-weight: 800; font-size: 34px; line-height: 42px; }
  .offer-text { font-size: 15px; line-height: 18px; }
  .offer-text strong { color: var(--brand-green); }
  .offer-price { font-size: 29px; font-weight: 700; line-height: 39px; margin-top: 8px; }
  .offer-price span { color: var(--brand-green); }
  .offer-note { font-size: 11px; line-height: 14px; margin-top: 1px; }
  .scene { position: absolute; left: 0; top: 0; }
  .website {
    position: absolute; left: 750px; top: 628px; width: 370px;
    text-align: center;
    color: var(--brand-green);
    font-weight: 700;
    font-size: 24px;
    line-height: 30px;
  }
  .brand-box {
    position: absolute; left: 750px; top: 668px;
    width: 370px; height: 152px;
    background: var(--white);
    padding: 6px;
  }
  .brand-box-inner {
    height: 100%;
    background: var(--brand-green);
    display: flex; align-items: center; gap: 16px;
    padding-left: 28px;
  }
  .brand-mark { width: 40px; height: 40px; background: var(--white); flex: none; }
  .brand-name { color: var(--white); font-weight: 700; font-size: 26px; line-height: 32px; }
  .address {
    position: absolute; left: 740px; top: 831px; width: 394px;
    text-align: center;
    font-weight: 700; font-size: 19px; line-height: 26px;
  }
  .call {
    position: absolute; left: 97px; top: 797px; width: 560px;
    text-align: center;
  }
  .call-line { color: var(--white); font-weight: 700; font-size: 30px; line-height: 44px; }
  .call-line .phone { color: var(--brand-green); font-size: 40px; }
  .email { font-weight: 700; font-size: 19px; line-height: 26px; margin-top: 4px; }
</style>
</head>
<body>
<main class="ad">
  <div class="circuit-backdrop" role="img" aria-label="Faint white circuit-board line pattern across the light grey background"></div>

  <h1 class="headline">Looking for Great<br>Computer Service?</h1>
  <p class="subhead">You’re in the Right Place!</p>

  <h2 class="services-label">Our Services:</h2>
  <ul class="services-list">
    <li><svg width="15" height="15" viewBox="0 0 15 15"><rect width="15" height="15" fill="var(--brand-orange)"/><path d="M3 7.5l3 3 6-7" stroke="#fff" stroke-width="2" fill="none"/></svg>New Computers and Laptops</li>
    <li><svg width="15" height="15" viewBox="0 0 15 15"><rect width="15" height="15" fill="var(--brand-orange)"/><path d="M3 7.5l3 3 6-7" stroke="#fff" stroke-width="2" fill="none"/></svg>Computer and Laptop Repairs</li>
    <li><svg width="15" height="15" viewBox="0 0 15 15"><rect width="15" height="15" fill="var(--brand-orange)"/><path d="M3 7.5l3 3 6-7" stroke="#fff" stroke-width="2" fill="none"/></svg>Fixed Price Computer and<br>Network Complete Management</li>
    <li><svg width="15" height="15" viewBox="0 0 15 15"><rect width="15" height="15" fill="var(--brand-orange)"/><path d="M3 7.5l3 3 6-7" stroke="#fff" stroke-width="2" fill="none"/></svg>Backup and Virus Protection</li>
    <li><svg width="15" height="15" viewBox="0 0 15 15"><rect width="15" height="15" fill="var(--brand-orange)"/><path d="M3 7.5l3 3 6-7" stroke="#fff" stroke-width="2" fill="none"/></svg>Internet Services</li>
    <li><svg width="15" height="15" viewBox="0 0 15 15"><rect width="15" height="15" fill="var(--brand-orange)"/><path d="M3 7.5l3 3 6-7" stroke="#fff" stroke-width="2" fill="none"/></svg>Printer Sales and Repairs</li>
    <li><svg width="15" height="15" viewBox="0 0 15 15"><rect width="15" height="15" fill="var(--brand-orange)"/><path d="M3 7.5l3 3 6-7" stroke="#fff" stroke-width="2" fill="none"/></svg>Data Recovery</li>
  </ul>

  <section class="offer">
    <p class="offer-title">SPECIAL OFFER!</p>
    <p class="offer-text">Get our special <strong>High Tech Tune Up</strong><br>for any of your computers or servers<br>for a special low rate of:</p>
    <p class="offer-price"><span>$99</span> per PC<br><span>$158</span> per server</p>
    <p class="offer-note">Call us for details and a list of included services.</p>
  </section>

  <svg class="scene" width="1200" height="885" viewBox="0 0 1200 885">
    <defs>
      <linearGradient id="case-tone" x1="0" y1="0" x2="1" y2="0">
        <stop offset="0" stop-color="var(--case-dark)"/>
        <stop offset="0.24" stop-color="var(--case-mid)"/>
        <stop offset="0.48" stop-color="var(--case-dark)"/>
        <stop offset="0.52" stop-color="var(--case-dark)"/>
        <stop offset="0.76" stop-color="var(--case-mid)"/>
        <stop offset="1" stop-color="var(--case-dark)"/>
      </linearGradient>
    </defs>
    <rect class="product-photo" x="28" y="393" width="425" height="400" fill="url(#case-tone)" role="img" aria-label="Two black gaming tower PC cases with hexagonal front grilles"/>
    <path d="M0 640 C260 745 520 770 760 745 C940 726 1080 718 1200 712 L1200 885 L0 885 Z" fill="var(--brand-green)"/>
    <path d="M0 680 C260 775 520 790 760 768 C940 750 1080 744 1200 740 L1200 885 L0 885 Z" fill="var(--brand-orange)"/>
  </svg>

  <p class="website">www.cwtbellbrook.example</p>

  <div class="brand-box">
    <div class="brand-box-inner">
      <span class="brand-mark"></span>
      <span class="brand-name">Circuitwise<br>Technicians</span>
    </div>
  </div>

  <p class="address">87B Harbour Street, Bellbrook, NSW, 2440</p>

  <div class="call">
    <p class="call-line">Call Us Today <span class="phone">(02) 5550 1842</span></p>
    <p class="email">admin@cwtbellbrook.example</p>
  </div>
</main>
</body>
</html>
```